Security Company Needs a Website *

We need a website that gives our clients information about the services we provide, methods of contacting us and landing page to advertise on social media sites.

We need five landing pages titled Home, About Us, Services, Contact Us and a Landing Page that can be linked to Chatterlane advertising.

About Us - Should have a section for Core Values & Ethics, Our Vision, Our Mission and Partners.

Services - This page should show the different categories which include CCTV, Security Alarms, Access Control and Fire Protection.

CCTV Service Description:
Closed circuit television (CCTV) has long been implemented by businesses as a surveillance tool in areas that need monitoring. With digital CCTV cameras, multiple video cameras transmit signals through a set of monitors. The cameras provide thorough surveillance of the area.

With vast technological improvements over the last ten years, businesses with CCTV systems can use unique IP cameras and video analytics to monitor traffic flows, people-count, implement facial and number plate recognition. Useful information about customer behaviour and demographics can be discovered too. CCTV helps prevent crime in many industries and can assist with the improvement of industrial processes, safety on transport systems and traffic monitoring.

Security Alarms Service Description:
Alarms systems are electronic devices programmed to alert people to specific dangers and detect intrusions, fire or theft. Security alarms, systems and access control monitoring combine to create an integrated surveillance solution, tailored to your business’ unique requirements. Our surveillance and alarm monitoring services are ideal for perimeter protection from unwanted intruders or potential dangers.

Access Control Services:
An access control system allows for the free flow of authorised personnel while denying entry to unwanted visitors. With walk-in thieves and trespassers shut out, you dramatically reduce your exposure to crime while increasing the security of your employees, visitors, information and assets.

* Control when and who is entering your premises
* Protect employees, assets and information
* Secure an area or sector
* Observe movement
* Integrate with other security systems

Our range of access control systems can be seamlessly linked to other systems in our portfolio. These include Fire Detection Systems, Intruder Alarms, CCTV, and Building Management. A common request involves the need for a CCTV camera to pan around and focus on a door that has been highlighted as a security risk by the access control system.

Fire Protection Service:
To Be Advised

The above copy-writing will also have to be changed.

Contact Us - This form needs to be simple and straightforward to gather the prospects information and we would like to have a call to action on this page. The Contact Us page should also have a wayfindr plot location of our office address.

We would also like to have a link to our chatterlane page on the website.

Target Market(s)

Commercial businesses, building construction developers and property managers.

Industry/Entity Type

Security

Number of Pages Required

5+ page

Font styles to use
Sans Serif

Colors

Designer to choose colors to be used in the design.

Requirements
Must have
• We need to have the same look and feel as well as website features as the following website:
• https://www.kovrangard.com.au/business-security/
• The website must be easy to use and easy to edit as well.

```html
<!DOCTYPE html>
<html lang="en">
<head>
<meta charset="utf-8">
<title>Nocturne Security Solutions</title>
<link href="https://fonts.googleapis.com/css2?family=Montserrat:wght@500;600;700;800&family=Open+Sans:wght@400;600;700&display=swap" rel="stylesheet">
<style>
:root{
  --navy:#1c2d86;
  --blue:#1d3b9e;
  --ink:#222;
  --muted:#555;
  --line:#cfcfcf;
  --pale:#f4f1f0;
  --pale2:#eceae7;
  --card:#f8f5f4;
  --white:#fff;
}
*{box-sizing:border-box;margin:0;padding:0}
html,body{width:1200px;height:3571px;overflow:hidden}
body{position:relative;background:var(--white);font-family:"Open Sans",Arial,sans-serif;color:var(--ink)}
.btn{position:absolute;background:var(--blue);color:var(--white);font-family:"Montserrat",Arial,sans-serif;font-weight:700;font-size:11px;letter-spacing:.5px;display:flex;align-items:center;justify-content:center}
.section-title{position:absolute;left:0;width:1200px;text-align:center;font-family:"Montserrat",Arial,sans-serif;font-weight:800;font-size:29px;color:var(--navy);letter-spacing:.5px}
.title-rule{position:absolute;height:3px;background:#d6d6d6}

/* header */
.site-header{position:absolute;left:0;top:0;width:1200px;height:120px;background:var(--white);z-index:3}
.logo-badge{position:absolute;left:134px;top:0;width:160px;height:156px;background:var(--white);border-radius:0 0 80px 80px;z-index:4;display:flex;flex-direction:column;align-items:center;padding-top:14px}
.logo-dot{width:82px;height:82px;border-radius:50%;background:var(--navy)}
.logo-name{margin-top:8px;font-family:"Montserrat",Arial,sans-serif;font-weight:700;font-size:15px;color:var(--navy);letter-spacing:1px}
.call{position:absolute;left:688px;top:24px;display:flex;align-items:center;gap:10px}
.call small{display:block;font-family:"Montserrat",Arial,sans-serif;font-weight:700;font-size:10px}
.call strong{font-family:"Montserrat",Arial,sans-serif;font-weight:700;font-size:18px;color:var(--navy)}
.follow{position:absolute;left:905px;top:34px;font-family:"Montserrat",Arial,sans-serif;font-weight:700;font-size:10px}
.social{position:absolute;display:flex;gap:8px}
.social span{width:26px;height:26px;border-radius:50%;background:var(--blue)}
.social span:nth-child(2){background:#1da1f2}
.social span:nth-child(3){background:#1a2050}
.main-nav{position:absolute;left:690px;top:78px;display:flex;font-family:"Montserrat",Arial,sans-serif;font-weight:700;font-size:12px}
.main-nav a{color:var(--ink);text-decoration:none;padding:6px 10px;margin-right:22px}
.main-nav a.active{background:var(--navy);color:var(--white)}

/* hero */
.hero{position:absolute;left:0;top:120px;width:1200px;height:554px;background:linear-gradient(90deg,#8b8784 0%,#5c5a58 25%,#3b3a3a 50%,#6f6b67 75%,#a59f98 100%)}
.hero-label{position:absolute;left:793px;top:278px;height:44px;padding:0 10px;background:var(--navy);color:var(--white);font-family:"Montserrat",Arial,sans-serif;font-weight:700;font-size:26px;display:flex;align-items:center}
.hero-title{position:absolute;left:793px;top:328px;color:var(--white);font-family:"Montserrat",Arial,sans-serif;font-weight:800;font-size:46px;line-height:50px;letter-spacing:1px}
.dots{position:absolute;left:560px;top:604px;display:flex;gap:14px;align-items:center}
.dots span{width:9px;height:9px;border-radius:50%;background:var(--white)}
.dots span.on{width:14px;height:14px;background:transparent;border:2px solid var(--white)}

/* about */
.about-title{position:absolute;left:155px;top:808px;font-family:"Montserrat",Arial,sans-serif;font-weight:800;font-size:29px;color:var(--navy)}
.about-text{position:absolute;left:155px;top:903px;width:295px;font-size:11.5px;line-height:15.5px;color:var(--muted);text-align:justify}
.tree-line{position:absolute;background:var(--line)}
.center-badge{position:absolute;left:541px;top:905px;width:114px;height:114px;border-radius:50%;background:var(--navy);display:flex;align-items:center;justify-content:center;color:var(--white);font-family:"Montserrat",Arial,sans-serif;font-weight:700;font-size:17px;letter-spacing:1px}
.value-icon{position:absolute;width:62px;height:62px;border-radius:50%;background:var(--navy);display:flex;align-items:center;justify-content:center}
.value{position:absolute;left:812px;width:260px}
.value h3{font-family:"Montserrat",Arial,sans-serif;font-weight:700;font-size:12px;margin-bottom:8px}
.value p{font-size:11px;line-height:14px;color:var(--muted)}

/* services */
.services{position:absolute;left:0;top:1314px;width:1200px;height:700px;background:var(--pale)}
.service-img{position:absolute;top:1520px;width:220px;height:220px;border-radius:50%}
.service-name{position:absolute;width:320px;text-align:center;top:1793px;font-family:"Montserrat",Arial,sans-serif;font-weight:700;font-size:15px}
.service-text{position:absolute;width:320px;text-align:center;top:1834px;font-size:11.5px;line-height:17px;color:var(--muted)}

/* fire */
.fire-img{position:absolute;left:0;top:2014px;width:619px;height:429px;background:radial-gradient(circle at 50% 45%,#d8dcde 0%,#b9c3c8 45%,#7d8d96 100%)}
.fire-copy{position:absolute;left:619px;top:2014px;width:581px;height:429px;background:var(--pale2)}
.fire-copy h3{position:absolute;left:0;width:581px;top:124px;text-align:center;font-family:"Montserrat",Arial,sans-serif;font-weight:700;font-size:17px}
.fire-copy p{position:absolute;left:110px;width:361px;top:172px;text-align:center;font-size:11.5px;line-height:16px;color:var(--muted)}

/* contact */
.contact-card{position:absolute;left:133px;top:2690px;width:934px;height:484px;background:var(--white);box-shadow:0 4px 24px rgba(0,0,0,.12)}
.contact-info{position:absolute;left:0;top:0;width:446px;height:484px;background:var(--card)}
.info-icon{position:absolute;left:66px;width:30px;height:30px;border-radius:50%;background:var(--navy);display:flex;align-items:center;justify-content:center}
.info{position:absolute;left:129px;font-size:12px;line-height:18px;color:var(--ink)}
.info b{display:block;font-family:"Montserrat",Arial,sans-serif;font-size:10.5px;margin-bottom:6px}
.info-rule{position:absolute;left:66px;width:335px;height:1px;background:#ddd}
.form-title{position:absolute;left:507px;top:57px;font-family:"Montserrat",Arial,sans-serif;font-weight:700;font-size:14px}
.field{position:absolute;left:507px;width:358px;height:36px;border:1px solid #bbb;background:var(--white);font-size:10.5px;color:#444;padding:9px 10px}

/* footer */
.site-footer{position:absolute;left:0;top:3298px;width:1200px;height:273px;background:var(--navy)}
.footer-badge{position:absolute;left:538px;top:3240px;width:124px;height:124px;border-radius:50%;background:var(--white);display:flex;align-items:center;justify-content:center}
.footer-badge span{width:104px;height:104px;border-radius:50%;background:var(--navy);display:flex;align-items:center;justify-content:center;color:var(--white);font-family:"Montserrat",Arial,sans-serif;font-weight:700;font-size:14px;letter-spacing:1px}
.footer-name{position:absolute;left:0;width:1200px;top:3376px;text-align:center;color:var(--white);font-family:"Montserrat",Arial,sans-serif;font-weight:500;font-size:16px;line-height:20px}
.footer-tag{position:absolute;left:0;width:1200px;top:3397px;text-align:center;color:var(--white);font-size:9px;line-height:12px;letter-spacing:.5px}
.footer-nav{position:absolute;left:0;width:1200px;top:3449px;text-align:center;color:var(--white);font-family:"Montserrat",Arial,sans-serif;font-weight:700;font-size:11px;word-spacing:3px}
.footer-rule{position:absolute;left:420px;width:360px;top:3484px;height:1px;background:rgba(255,255,255,.2)}
.copyright{position:absolute;left:0;width:1200px;top:3507px;text-align:center;color:var(--white);font-size:10.5px}
</style>
</head>
<body>

<header class="site-header">
  <div class="call">
    <svg width="22" height="22" viewBox="0 0 24 24"><circle cx="12" cy="12" r="12" fill="#1c2d86"/><path d="M8.5 6.5l2 2-1.2 1.6c.8 1.6 2 2.8 3.6 3.6l1.6-1.2 2 2-1.3 1.7c-3.7-.4-7.6-4.3-8-8z" fill="#fff"/></svg>
    <div><small>CALL US</small><strong>555.010.2040</strong></div>
  </div>
  <div class="follow">FOLLOW US</div>
  <div class="social" style="left:978px;top:28px"><span></span><span></span><span></span></div>
  <nav class="main-nav">
    <a class="active">HOME</a><a>ABOUT US</a><a>SERVICES</a><a>CONTACT US</a>
  </nav>
</header>
<div class="logo-badge"><div class="logo-dot"></div><div class="logo-name">NOCTURNE</div></div>

<section class="hero" role="img" aria-label="Photo of a fingerprint access control keypad mounted beside a glass office door"></section>
<div class="hero-label">ACCESS CONTROL</div>
<div class="hero-title">SECURITY<br>SOLUTIONS</div>
<div class="btn" style="left:793px;top:460px;width:131px;height:38px;font-size:13px">READ MORE</div>
<div class="dots"><span></span><span></span><span class="on"></span><span></span><span></span></div>

<h2 class="about-title">ABOUT US</h2>
<div class="title-rule" style="left:155px;top:855px;width:150px;height:2px"></div>
<p class="about-text">On the other hand, we denounce with righteous indignation and dislike men who are so beguiled and demoralized by the charms of pleasure of the moment, so blinded by desire, that they cannot foresee the pain and trouble that are bound to ensue; and equal blame belongs to those who fail in their duty through weakness.</p>
<div class="btn" style="left:157px;top:1076px;width:112px;height:40px">READ MORE</div>

<div class="tree-line" style="left:598px;top:795px;width:1px;height:372px"></div>
<div class="tree-line" style="left:598px;top:795px;width:132px;height:1px"></div>
<div class="tree-line" style="left:598px;top:910px;width:132px;height:1px"></div>
<div class="tree-line" style="left:598px;top:1036px;width:132px;height:1px"></div>
<div class="tree-line" style="left:598px;top:1167px;width:132px;height:1px"></div>
<div class="center-badge">NOCTURNE</div>

<div class="value-icon" style="left:729px;top:764px"><svg width="30" height="26" viewBox="0 0 30 26"><path d="M7 2h16l6 7-14 15L1 9z" fill="none" stroke="#fff" stroke-width="2"/><path d="M1 9h28M10 2l-3 7 8 15 8-15-3-7" fill="none" stroke="#fff" stroke-width="1.5"/></svg></div>
<div class="value" style="top:766px"><h3>CORE VALUES &amp; ETHICS</h3><p>Sed ut perspiciatis unde omnis iste natus error sit voluptatem accusantium doloremque</p></div>

<div class="value-icon" style="left:729px;top:879px"><svg width="32" height="20" viewBox="0 0 32 20"><path d="M1 10C6 2 26 2 31 10 26 18 6 18 1 10z" fill="none" stroke="#fff" stroke-width="2"/><circle cx="16" cy="10" r="5" fill="#fff"/></svg></div>
<div class="value" style="top:881px"><h3>OUR VISION</h3><p>Sed ut perspiciatis unde omnis iste natus error sit voluptatem accusantium doloremque</p></div>

<div class="value-icon" style="left:729px;top:1005px"><svg width="30" height="22" viewBox="0 0 30 22"><path d="M1 21L13 4l5 7 3-4 8 14z" fill="#fff"/></svg></div>
<div class="value" style="top:1007px"><h3>OUR MISSION</h3><p>Sed ut perspiciatis unde omnis iste natus error sit voluptatem accusantium doloremque</p></div>

<div class="value-icon" style="left:729px;top:1131px"><svg width="30" height="26" viewBox="0 0 30 26"><circle cx="8" cy="6" r="4" fill="#fff"/><circle cx="22" cy="6" r="4" fill="#fff"/><circle cx="15" cy="9" r="4" fill="#fff"/><path d="M2 25v-9c0-3 3-5 6-5s6 2 6 5v9zM16 25v-9c0-3 3-5 6-5s6 2 6 5v9z" fill="#fff"/></svg></div>
<div class="value" style="top:1133px"><h3>PARTNERS</h3><p>Sed ut perspiciatis unde omnis iste natus error sit voluptatem accusantium doloremque</p></div>

<section class="services"></section>
<h2 class="section-title" style="top:1388px">SERVICES</h2>
<div class="title-rule" style="left:527px;top:1435px;width:146px"></div>

<div class="service-img" role="img" aria-label="Photo of a white CCTV camera" style="left:140px;background:radial-gradient(circle,#e9eaec 0%,#c9cdd2 60%,#f4f1f0 72%)"></div>
<div class="service-img" role="img" aria-label="Photo of a white ceiling smoke alarm" style="left:490px;background:radial-gradient(circle,#f2f2f2 0%,#d8d8d8 60%,#f4f1f0 72%)"></div>
<div class="service-img" role="img" aria-label="Photo of a fingerprint access control terminal" style="left:833px;background:radial-gradient(circle,#3a3a3c 0%,#8a8b8e 55%,#f4f1f0 72%)"></div>

<div class="service-name" style="left:90px">CCTV</div>
<p class="service-text" style="left:90px">Closed circuit television (CCTV) has long been<br>implemented by businesses...</p>
<div class="btn" style="left:210px;top:1895px;width:86px;height:26px">READ MORE</div>

<div class="service-name" style="left:440px">SECURITY ALARMS</div>
<p class="service-text" style="left:440px">Alarms systems are electronic devices programmed<br>to alert people to specific dangers and..</p>
<div class="btn" style="left:552px;top:1895px;width:86px;height:26px">READ MORE</div>

<div class="service-name" style="left:783px">ACCESS CONTROL</div>
<p class="service-text" style="left:783px">An access control system allows for the free flow<br>of authorised personnel while denying ...</p>
<div class="btn" style="left:897px;top:1895px;width:86px;height:26px">READ MORE</div>

<div class="fire-img" role="img" aria-label="Close-up photo of a ceiling fire sprinkler head with a red glass bulb"></div>
<div class="fire-copy">
  <h3>FIRE PROTECTION</h3>
  <p>At vero eos et accusamus et iusto odio dignissimos ducimus qui blanditiis praesentium voluptatum deleniti atque corrupti quos dolores et quas molestias excepturi sint occaecati</p>
</div>
<div class="btn" style="left:833px;top:2289px;width:86px;height:26px">READ MORE</div>

<h2 class="section-title" style="top:2545px">CONTACT US</h2>
<div class="title-rule" style="left:508px;top:2594px;width:184px"></div>

<div class="contact-card">
  <div class="contact-info">
    <div class="info-icon" style="top:74px"><svg width="12" height="16" viewBox="0 0 12 16"><path d="M6 0a6 6 0 0 1 6 6c0 4-6 10-6 10S0 10 0 6a6 6 0 0 1 6-6z" fill="#fff"/><circle cx="6" cy="6" r="2.2" fill="#1c2d86"/></svg></div>
    <div class="info" style="top:70px"><b>ADDRESS</b>2217 Birch Lane<br>Harbor Vale, NY 11602</div>
    <div class="info-rule" style="top:150px"></div>

    <div class="info-icon" style="top:183px"><svg width="14" height="14" viewBox="0 0 24 24"><path d="M5 3l4 4-2.2 2.8c1.5 3 3.6 5.1 6.4 6.4L16 14l4 4-2.4 3C10 20.5 3.5 14 3 5.4z" fill="#fff"/></svg></div>
    <div class="info" style="top:182px"><b>PHONE</b>555.010.2040</div>
    <div class="info-rule" style="top:245px"></div>

    <div class="info-icon" style="top:278px"><svg width="14" height="11" viewBox="0 0 14 11"><rect width="14" height="11" rx="1" fill="#fff"/><path d="M0 1l7 5 7-5" fill="none" stroke="#1c2d86" stroke-width="1.4"/></svg></div>
    <div class="info" style="top:277px"><b>E MAIL</b>info@nocturnesecurity.com</div>

    <div class="info" style="top:373px;left:64px"><b>FOLLOW US ON</b></div>
    <div class="social" style="left:64px;top:404px"><span></span><span></span><span></span></div>
  </div>
  <div class="form-title">SEND MESSAGE</div>
  <div class="field" style="top:98px">Name</div>
  <div class="field" style="top:146px">E mail id</div>
  <div class="field" style="top:193px">Phone</div>
  <div class="field" style="top:241px;height:121px">Message</div>
  <div class="btn" style="left:507px;top:386px;width:93px;height:36px;font-size:12px">SUBMIT</div>
</div>

<footer class="site-footer"></footer>
<div class="footer-badge"><span>NOCTURNE</span></div>
<div class="footer-name">SECURITY SOLUTIONS</div>
<div class="footer-tag">EXCEEDING EXPECTATIONS</div>
<nav class="footer-nav">HOME &nbsp;| &nbsp;ABOUT US &nbsp;| &nbsp;SERVICES &nbsp;| &nbsp;CONTACT US</nav>
<div class="footer-rule"></div>
<p class="copyright">Copyrights @ 2018 All Rights Reserved</p>

</body>
</html>
```